Consulting company, design, Interior design in commercial real estate (Tertiai sector *

Company name: VORANDEL: from the Greek Evexia well-being, was born from a desire to combine well-being and work. By the choice of design, materials, design and furniture, everything is thought from this perspective

Logo: Essay with Möbius Ribbon and / or with the infinite acronym / and or triangle ...
Sentences to write:
"The exclusive partner for your development projects"
"Consulting - Design - Construction"
"We manage EVERYTHING for you"

On the back: Photo (attached; if photo is not clear, another photo can be provided) with company name and "VORANDEL, Excellence and reliability"
My name / First name: provided later (double name), Manager
Address: supplied later
Tel: supplied later
Website: www. vorandel.com
Colors: Black, gold and white. Other admissible colors
See attached files

Real estate business

Nom de l'entreprise : VORANDEL : du grec Evexia bien être, est né d'une volonté de faire rimer bien être et travail. Par le choix de la conception, des matériaux, du design et du mobilier, tout est pensé dans cette optique

Logo : Essai avec Ruban de Möbius et /ou avec le sigle infini / et ou triangle...
Phrases à inscrire :
"Le partenaire exclusif de vos projets d'aménagement"
"Conseil - Conception - Construction"
"Nous gérons TOUT pour vous"

Au verso : Photo (ci-jointe ; si photo pas nette, une autre photo peut être fournie) avec nom de l'entreprise et Mention "VORANDEL, Excellence et fiabilité"
Mon nom / Prénom : fourni ultérieurement (prénom double), Gérant
Adresse : fourni ultérieurement
Tél : fourni ultérieurement
Site Web : www. vorandel.com
Couleurs : Noir, doré et blanc. Autre couleurs recevables
Voir fichiers ci-joint

• My project must be simple, clear, neat and design.
The business card must catch the customer

```html
<!DOCTYPE html>
<html lang="en">
<head>
<meta charset="utf-8">
<title>Vorandel Business Card</title>
<link rel="stylesheet" href="https://fonts.googleapis.com/css2?family=Montserrat:wght@400;500;600&family=Oswald:wght@400;500;600&display=swap">
<style>
  :root {
    --backdrop: #2a2a2c;
    --card: #0b0b0b;
    --gold: #d9a520;
    --gold-soft: #b8891a;
    --white: #ffffff;
    --muted: #e6e6e6;
  }
  * { margin: 0; padding: 0; box-sizing: border-box; }
  html, body { width: 1200px; height: 900px; overflow: hidden; }
  body {
    background: var(--backdrop);
    position: relative;
    font-family: "Montserrat", Arial, sans-serif;
    color: var(--white);
  }
  .card {
    position: absolute;
    width: 640px;
    height: 366px;
    background: var(--card);
    box-shadow: 0 14px 30px rgba(0,0,0,.55);
    overflow: hidden;
  }
  .card--front { left: 50px; top: 70px; }
  .card--back { left: 510px; top: 464px; }

  /* brand block */
  .brand { display: flex; flex-direction: column; align-items: center; }
  .brand__name {
    display: flex; align-items: center; gap: 12px;
    font-family: "Montserrat", Arial, sans-serif;
    font-weight: 500;
    font-size: 38px;
    letter-spacing: 3px;
    color: var(--white);
    line-height: 1;
  }
  .brand__mark { width: 22px; height: 22px; background: var(--gold); }
  .brand__tagline {
    display: flex; align-items: center; gap: 8px;
    margin-top: 7px;
    font-size: 10.5px;
    letter-spacing: 1px;
    text-transform: uppercase;
    color: var(--gold);
    font-weight: 500;
  }
  .brand__tagline::before, .brand__tagline::after {
    content: ""; width: 22px; height: 1px; background: var(--gold);
  }

  /* front */
  .front__brand { position: absolute; top: 70px; left: 0; right: 0; }
  .front__copy {
    position: absolute; top: 176px; left: 0; right: 0;
    text-align: center;
    font-family: "Oswald", "Arial Narrow", sans-serif;
    text-transform: uppercase;
  }
  .front__intro { font-size: 15px; font-weight: 500; letter-spacing: .6px; }
  .front__services { font-size: 29px; font-weight: 600; letter-spacing: .8px; margin-top: 2px; }
  .front__promise { font-size: 13px; font-weight: 400; letter-spacing: .8px; margin-top: 16px; }
  .front__rule {
    position: absolute; top: 318px; left: 230px;
    width: 180px; height: 3px; background: var(--gold);
  }

  /* back */
  .back__brand { position: absolute; top: 36px; right: 56px; }
  .back__person { position: absolute; top: 112px; right: 56px; text-align: right; }
  .back__name {
    font-size: 26px; font-weight: 500; letter-spacing: 2px; text-transform: uppercase; line-height: 1;
  }
  .back__role { font-size: 13px; margin-top: 4px; color: var(--muted); }
  .back__rule {
    position: absolute; top: 184px; left: 350px; width: 250px; height: 1px; background: var(--gold-soft);
  }
  .back__address {
    position: absolute; top: 220px; right: 40px; text-align: right;
    font-size: 14px; line-height: 1.4; color: var(--muted); font-style: normal;
  }
  .back__photo {
    position: absolute; left: 96px; top: 104px; width: 230px; height: 168px;
    background: radial-gradient(ellipse at 45% 35%, #8a6b58 0%, #4a4a55 45%, #1c2333 75%, #0b0b0b 100%);
  }
  .contact {
    position: absolute; left: 120px; top: 284px;
    list-style: none;
    font-size: 13.5px; line-height: 1;
  }
  .contact__item { display: flex; align-items: center; gap: 9px; margin-bottom: 6px; }
  .contact__icon { width: 13px; height: 13px; flex: none; }
</style>
</head>
<body>

  <section class="card card--front">
    <div class="brand front__brand">
      <div class="brand__name"><span class="brand__mark"></span>VORANDEL</div>
      <div class="brand__tagline">Excellence and reliability</div>
    </div>
    <div class="front__copy">
      <p class="front__intro">The exclusive partner for your development projects</p>
      <p class="front__services">Consulting - Design - Construction</p>
      <p class="front__promise">We manage everything for you</p>
    </div>
    <div class="front__rule"></div>
  </section>

  <section class="card card--back">
    <div class="back__photo" role="img" aria-label="Portrait photo of the manager in a dark suit"></div>

    <div class="brand back__brand">
      <div class="brand__name"><span class="brand__mark"></span>VORANDEL</div>
      <div class="brand__tagline">Excellence and reliability</div>
    </div>

    <div class="back__person">
      <p class="back__name">Marc Delorme</p>
      <p class="back__role">Manager</p>
    </div>

    <div class="back__rule"></div>

    <address class="back__address">
      00000 Harlow Avenue, Suite 000<br>
      Eastbrook, ON, L0C 000
    </address>

    <ul class="contact">
      <li class="contact__item">
        <svg class="contact__icon" viewBox="0 0 24 24" fill="var(--gold)"><path d="M6.6 10.8a15.1 15.1 0 0 0 6.6 6.6l2.2-2.2c.3-.3.7-.4 1-.2 1.1.4 2.3.6 3.6.6.6 0 1 .4 1 1V20c0 .6-.4 1-1 1A17 17 0 0 1 3 4c0-.6.4-1 1-1h3.5c.6 0 1 .4 1 1 0 1.3.2 2.5.6 3.6.1.3 0 .7-.2 1z"/></svg>
        <span>000-000-0000</span>
      </li>
      <li class="contact__item">
        <svg class="contact__icon" viewBox="0 0 24 24" fill="none" stroke="var(--gold)" stroke-width="2"><path d="M2 5h20v14H2z"/><path d="M2 5l10 8 10-8"/></svg>
        <span>marc@delorme.com</span>
      </li>
      <li class="contact__item">
        <svg class="contact__icon" viewBox="0 0 24 24" fill="none" stroke="var(--gold)" stroke-width="2"><circle cx="12" cy="12" r="10"/><path d="M2 12h20M12 2c3 3 3 17 0 20M12 2c-3 3-3 17 0 20"/></svg>
        <span>www.vorandel.com</span>
      </li>
    </ul>
  </section>

</body>
</html>
```